Global Fuel Additive Business needs Letter Head, Envelope and matching business card.

Our company, Verdane Holdings Co. Ltd are manufacturers of an enzyme based fuel additive, serving major Japanese shipping companies and bunker fuel users.
Our product, Fenarix K-407T is made of natural enzymes which works on the core level of polymerized hydrocarbons by breaking them down into monomers by its organic enzymes. This reaction results in direct improvement in fuel quality for optimum combustion by increasing oxygen content within the fuel particles leading to benefits such as
Improving cleanliness of fuel tanks and surrounding systems
 Increasing combustion on Main/Aux engines and boilers
 Eliminating black smoke from exhaust
 Preventing soot accumulation in turbo-chargers and exhaust-gas economizer
 Reducing average fuel consumption by 3.5%

Our plan is to conduct an initial phase of international marketing targeting international shipping companies, oil companies and heavy machinery users. We will like to see designs which are in line with the current company image : http://www.verdaneholding.co.jp/en/index.html . The initial stage will include a direct mail campaign.

The final image should be a crisp version of what is already on the site. New ideas based the concept of our product being ecologically friendly, as it is produced from natural enzymes, are welcome.
Updates

Dear Participants to Fenarix Letterhead design. Thank you so much for participating. It was a difficult choice to pick one our of many competent design work but the decision had to be made. Will look forward for your participation if any other projects emerges within our organization. Pavel

Industry/Entity Type

Shipping

```html
<!DOCTYPE html>
<html lang="en">
<head>
<meta charset="utf-8">
<title>Verdane Holdings Letterhead</title>
<link href="https://fonts.googleapis.com/css2?family=Open+Sans:wght@400;600;700&display=swap" rel="stylesheet">
<style>
  :root {
    --backdrop: #e9eaec;
    --paper: #ffffff;
    --brand-green: #1e5a2b;
    --ink: #2b2b2b;
    --map-tint: #f1f2f1;
  }
  * { margin: 0; padding: 0; box-sizing: border-box; }
  html, body {
    width: 1200px; height: 800px; overflow: hidden;
    background: var(--backdrop);
    font-family: "Open Sans", Arial, sans-serif;
    color: var(--ink);
  }
  .letterhead {
    position: absolute; left: 332px; top: 20px;
    width: 537px; height: 760px;
    background: var(--paper);
    box-shadow: 0 4px 14px rgba(0,0,0,0.12);
  }
  .edge-band {
    position: absolute; left: 0; top: 0; bottom: 0; width: 9px;
    background: var(--brand-green);
  }
  .world-map {
    position: absolute; left: 110px; top: 110px; width: 400px; height: 300px;
    background: radial-gradient(ellipse at center, var(--map-tint) 0%, rgba(241,242,241,0) 70%);
  }
  .brand {
    position: absolute; right: 40px; top: 40px;
    display: flex; align-items: center; gap: 7px;
  }
  .brand-dot { width: 12px; height: 12px; border-radius: 50%; background: var(--brand-green); }
  .brand-name {
    font-size: 13px; font-weight: 700; color: var(--brand-green);
    text-transform: uppercase; letter-spacing: 0.2px;
  }
  .meta {
    position: absolute; left: 40px; top: 130px;
    font-size: 7.5px; line-height: 10px;
  }
  .meta-line { display: block; }
  .meta-label { font-weight: 700; color: var(--brand-green); }
  .salutation { margin-top: 10px; font-size: 7.5px; line-height: 14px; }
  .salutation-name { padding-left: 8px; }
  .body-copy {
    position: absolute; left: 120px; top: 130px; width: 375px;
    font-size: 7.5px; line-height: 10.5px; text-align: justify;
  }
  .body-copy p + p { margin-top: 10px; }
  .signoff {
    position: absolute; left: 40px; top: 560px;
    font-size: 8px; line-height: 10.5px;
  }
  .footer-name {
    position: absolute; left: 40px; top: 640px;
    font-size: 18px; font-weight: 700; color: var(--brand-green);
    text-transform: uppercase; letter-spacing: 0.2px;
  }
  .contacts {
    position: absolute; left: 282px; top: 636px;
    display: flex; gap: 16px; font-size: 6.5px; line-height: 8.5px;
  }
  .contact-title { font-size: 6.5px; font-weight: 700; color: var(--brand-green); text-transform: uppercase; }
</style>
</head>
<body>
  <article class="letterhead">
    <div class="edge-band"></div>
    <div class="world-map" role="img" aria-label="Faint dotted world map in the background"></div>

    <header class="brand">
      <span class="brand-dot"></span>
      <span class="brand-name">Verdane Holdings Co. Ltd</span>
    </header>

    <div class="meta">
      <span class="meta-line"><span class="meta-label">Date:</span> 12/06/2013</span>
      <span class="meta-line"><span class="meta-label">Re:</span> Mira Kessel</span>
      <span class="meta-line"><span class="meta-label">To:</span> Tomas Hale</span>
      <div class="salutation">
        <p>Dear</p>
        <p class="salutation-name">Tomas Hale</p>
      </div>
    </div>

    <section class="body-copy">
      <p>Lorem ipsum dolor sit amet, consectetur adipiscing elit. Maecenas nec tellus justo. Sed diam ligula, commodo sit amet bibendum ut, mollis eget justo. Aliquam erat volutpat. Donec tristique sodales neque vel molestie. Pellentesque quis justo erat, sit amet aliquet arcu. Suspendisse iaculis, mauris vestibulum lobortis convallis lorem, sed sagittis interdum justo, ut fermentum orci tempus eu odio. Curabitur vestibulum scelerisque magna turpis lacus vestibulum nec. Vestibulum tempus vehicula imperdiet. Pellentesque eget risus nulla. Phasellus ac odio massa, id porta orci. Quisque sapien elit, bibendum ac mollis a, luctus sed mauris. Morbi elementum vestibulum odio a dignissim. Cras suscipit pulvinar mauris vel auctor. Aenean ultrices bibendum sapien elementum congue. Donec vulputate aliquam mi, sit amet tincidunt erat sagittis eu.</p>
      <p>Integer in laoreet erat. Curabitur non ipsum arcu, sit amet pretium lacus. Morbi vulputate justo eu sem porttitor a lobortis lectus pharetra. Nullam risus quam, suscipit sed malesuada scelerisque, rhoncus vitae lorem. Mauris porttitor suscipit commodo. Nullam felis orci, tristique nec venenatis ut, ultricies vel leo. Donec enim enim, ultrices in egestas a, commodo nec risus. Nam quis erat augue, eu porttitor lectus. Aliquam laoreet luctus orci, non auctor velit fermentum quis. Nunc ultricies scelerisque hendrerit.</p>
      <p>Vestibulum ante ipsum primis in faucibus orci luctus et ultrices posuere cubilia Curae; Aenean bibendum accumsan justo quis rhoncus. Morbi quis commodo sapien. Praesent ipsum erat, aliquet at vulputate consectetur, aliquam sit amet nibh. Vestibulum ante ipsum primis in faucibus orci luctus et ultrices posuere cubilia Curae; Vivamus accumsan purus vel leo rhoncus lacinia. Etiam libero enim, convallis at faucibus sit amet, vehicula at purus. Maecenas adipiscing imperdiet auctor. Integer placerat ullamcorper adipiscing.</p>
    </section>

    <footer>
      <div class="signoff">
        <p>Sincerely</p>
        <p>Mira Kessel</p>
        <p>Executive Manager</p>
      </div>
      <p class="footer-name">Verdane Holdings</p>
      <div class="contacts">
        <div class="contact-item">
          <h4 class="contact-title">Telephone &amp; Fax</h4>
          <p>+1 (0) 40 318 552 7046</p>
          <p>+1 (0) 40 318 552 7047</p>
        </div>
        <div class="contact-item">
          <h4 class="contact-title">Adress</h4>
          <p>Street, Region, Country</p>
          <p>PO BOX 321</p>
        </div>
        <div class="contact-item">
          <h4 class="contact-title">Web</h4>
          <p>info@verdaneholding.co.jp</p>
          <p>www.verdaneholding.co.jp</p>
        </div>
      </div>
    </footer>
  </article>
</body>
</html>
```